Home page web design for a lawn specialist business

-The design must be based around the attached HPID (home page information design) called Turf Haven HPID. I've attached Word and PDF versions - these are the same. The table boxes are just for approximate placement of information and you can use boxes and bold shapes for this design.

All fonts used in the HPID are only examples - you can use any Google font you wish.

- Text that is in orange is for your information only. Text to go on the design is black. Some instructions are in the HPID. Please be creative!

-The design needs to be modern and exciting - colours are to be the green of the logo, and white ...and then choose dark green, or dark grey or black.

Logo - attached (it's not great quality but don't worry, we'll replace it later)

- I've provided the images for the galleries - they are labelled and will match the name in the HPID. Please use the supplied images!

- Examples of some websites that have great design... don't copy them please but they are similar in look to what we are after....
www.kelbrinworks.co.nz
http://www.rimsafe-guarding.co.nz/
http://www.brightnest.wb.gs/

Important: Width of content will be 1280 pixels when implemented as a web page but the winning design will need to supplied be on a 2000 pixel wide background so nav bars and background can extend outside the 1280 width.
Header height (without nav bar) 150-160 pixels.

We don't comment on individual designs but will choose a winning design promptly.

Industry/Entity Type

Business

Number of Pages Required

1 page

Font styles to use
Sans Serif

Requirements
Must have
• clean, modern, well-spaced design

```html
<!DOCTYPE html>
<html lang="en">
<head>
<meta charset="utf-8">
<title>Turf Haven – Lawn specialists</title>
<link href="https://fonts.googleapis.com/css2?family=Raleway:wght@400;500;600;700&family=Open+Sans:wght@400;600;700&display=swap" rel="stylesheet">
<style>
:root{
  --green:#1f8f1f;
  --green-dark:#0f6e12;
  --green-light:#2fa82c;
  --ink:#1a1a1a;
  --grey-text:#555;
  --panel:#ececec;
  --charcoal:#333335;
  --black:#050505;
  --white:#fff;
  --lawn:#3e8f2a;
  --soil:#6e5a4a;
}
*{box-sizing:border-box;margin:0;padding:0}
html,body{width:739px;height:1200px;overflow:hidden;background:var(--white)}
body{position:relative;font-family:"Open Sans",Arial,sans-serif;color:var(--ink)}
.abs{position:absolute}

/* header */
.header{left:0;top:0;width:739px;height:64px;background:var(--white)}
.brand{left:82px;top:12px;display:flex;align-items:center;gap:7px}
.brand-mark{width:34px;height:34px;background:var(--green)}
.brand-name{font-family:"Raleway",sans-serif;font-weight:700;font-size:19px;color:var(--green)}
.header-info{right:76px;top:8px;text-align:right;font-family:"Raleway",sans-serif;color:var(--ink);line-height:1.15}
.header-info .title{font-size:13px;font-weight:500}
.header-info .line{font-size:9.5px;font-weight:500}
.header-info .phone{font-size:12px;font-weight:600;letter-spacing:.5px}

/* nav */
.nav{left:0;top:64px;width:739px;height:23px;background:linear-gradient(var(--green-light),var(--green-dark));display:flex;justify-content:center}
.nav ul{list-style:none;display:flex;margin-left:-20px}
.nav li{font-family:"Raleway",sans-serif;font-size:9px;font-weight:500;color:var(--white);height:23px;line-height:23px;padding:0 11.4px;border-right:1px solid rgba(255,255,255,.35)}
.nav li:last-child{border-right:0;padding-left:14px}

/* hero */
.hero{left:0;top:87px;width:739px;height:218px;overflow:hidden}
.hero-lawn{left:0;top:0;width:369px;height:218px;background:linear-gradient(160deg,#c9c9c2 0%,#9bbf7a 30%,var(--lawn) 60%,#2f7a20 100%)}
.hero-soil{left:369px;top:0;width:370px;height:218px;background:linear-gradient(200deg,#cfcac0 0%,#8a7868 30%,var(--soil) 65%,#5a4638 100%)}
.hero-ring{left:305px;top:43px;width:134px;height:134px;border-radius:50%;background:rgba(255,255,255,.35)}
.hero-badge{left:323px;top:61px;width:98px;height:98px;border-radius:50%;background:#f4f4f4;display:flex;align-items:center;justify-content:center;text-align:center;font-family:"Raleway",sans-serif;font-size:23px;line-height:1.05;color:var(--ink)}

/* intro */
.intro{left:0;top:305px;width:739px;height:163px;background:var(--panel);text-align:center}
.intro h1{position:absolute;left:0;width:739px;top:21px;font-family:"Raleway",sans-serif;font-weight:500;font-size:12px;letter-spacing:.3px}
.intro .sub{position:absolute;left:0;width:739px;top:38px;font-family:"Raleway",sans-serif;font-size:8.5px}
.intro .body{position:absolute;left:92px;width:555px;top:58px;font-size:5.8px;line-height:1.72;color:var(--grey-text);text-transform:uppercase}
.btn{display:flex;align-items:center;justify-content:center;gap:5px;background:linear-gradient(var(--green-light),var(--green-dark));color:var(--white);font-size:6.2px;font-weight:700;text-transform:uppercase;letter-spacing:.2px}
.btn svg{width:6px;height:6px}
.intro .btn{position:absolute;left:337px;top:118px;width:70px;height:23px}

/* services */
.services{left:0;top:468px;width:739px;height:211px;background:var(--charcoal)}
.card{position:absolute;top:24px;width:113px;height:164px;background:var(--white);text-align:center}
.card .pic{position:absolute;left:12px;top:6px;width:89px;height:89px;border-radius:50%;border:2px solid var(--green)}
.card h3{position:absolute;left:4px;right:4px;top:99px;font-family:"Raleway",sans-serif;font-size:7px;font-weight:700;line-height:1.15}
.card p{position:absolute;left:8px;right:8px;font-size:5.4px;line-height:1.6;color:var(--grey-text)}

/* welcome */
.welcome{left:0;top:679px;width:739px;height:159px;background:var(--white)}
.video{left:91px;top:26px;width:163px;height:108px;background:linear-gradient(180deg,#b7c6c4 0%,#7aa55b 45%,#3f7f28 100%);border:2px solid #222}
.video-bar{left:91px;top:118px;width:163px;height:16px;background:linear-gradient(#3a3a3a,#111)}
.video-progress{left:122px;top:124px;width:88px;height:3px;background:#555;border-radius:2px}
.video-progress span{display:block;width:42px;height:3px;background:#d42020;border-radius:2px}
.video-play{left:157px;top:66px;width:26px;height:17px;background:#000;border-radius:3px}
.divider-v{left:278px;top:26px;width:1px;height:108px;background:#e0e0e0}
.welcome h2{position:absolute;left:300px;top:27px;font-family:"Raleway",sans-serif;font-size:12px;font-weight:700;color:var(--ink)}
.welcome h2 em{font-style:normal;font-size:9.5px;color:var(--green)}
.welcome .rule{left:300px;top:44px;width:364px;height:1px;background:#ccc}
.welcome .rule span{display:block;width:62px;height:2px;background:var(--green);margin-top:-1px}
.welcome .body{position:absolute;left:301px;top:53px;width:364px;font-size:6.4px;line-height:1.28;color:#333}
.welcome .btn{position:absolute;left:302px;top:114px;width:69px;height:21px}

/* testimonials */
.reviews{left:0;top:838px;width:739px;height:134px;background:linear-gradient(180deg,#1e2418 0%,#2c3a22 50%,#25321c 100%)}
.reviews blockquote{position:absolute;left:0;width:739px;top:22px;text-align:center;font-family:"Raleway",sans-serif;font-size:11px;color:var(--white);line-height:1.3}
.review{position:absolute;top:62px;width:150px}
.review .avatar{position:absolute;left:0;top:0;width:31px;height:31px;border-radius:50%;border:2px solid var(--green);background:linear-gradient(#a8b0a0,#6e7a62)}
.review .name{position:absolute;left:38px;top:11px;font-family:"Raleway",sans-serif;font-size:7px;font-weight:700;color:var(--white)}
.review .box{position:absolute;left:-1px;top:40px;width:143px;height:46px;background:var(--white);box-shadow:0 1px 3px rgba(0,0,0,.25);padding:6px 10px;font-size:5.6px;line-height:1.65;color:#333}
.review .box:before{content:"";position:absolute;left:16px;top:-5px;border:5px solid transparent;border-top:0;border-bottom-color:var(--white)}

/* footer */
.footer{left:0;top:1015px;width:739px;height:165px;background:var(--black);color:var(--white)}
.footer h4{position:absolute;left:90px;top:21px;font-family:"Raleway",sans-serif;font-size:10px;font-weight:500}
.footer .links{position:absolute;left:91px;top:41px;list-style:none;font-size:6.8px;line-height:10.1px}
.footer .sep{position:absolute;top:22px;width:1px;height:118px;background:linear-gradient(transparent,#2a4a22,transparent)}
.tree{left:238px;top:18px;width:95px;height:88px;border-radius:46% 54% 40% 50%;background:radial-gradient(circle at 45% 40%,#a7d63c,#6ea92a 70%,#3d6e1a)}
.footer .diploma{position:absolute;left:220px;width:145px;top:114px;text-align:center;font-family:"Raleway",sans-serif;font-size:9px;color:#ddd}
.footer .quote{position:absolute;left:422px;top:22px;font-family:"Raleway",sans-serif;font-size:9.5px;font-weight:500;line-height:1.15;letter-spacing:.3px}
.field{position:absolute;background:var(--white);height:18px;font-size:6px;color:#aaa;padding:5px 7px}
.submit{left:597px;top:1154px;width:53px;height:17px;background:var(--green);color:var(--white);font-size:7px;display:flex;align-items:center;justify-content:center}
.copyright{left:0;top:1180px;width:739px;height:20px;background:var(--charcoal);color:#ddd;font-size:6.6px;line-height:20px;padding-left:90px}
</style>
</head>
<body>

<header class="abs header">
  <div class="abs brand"><span class="brand-mark"></span><span class="brand-name">Turf Haven</span></div>
  <div class="abs header-info">
    <div class="title">Lawn specialists</div>
    <div class="line">from ground preparation to lawnaftercare</div>
    <div class="line">Servicing the Auckland region</div>
    <div class="phone">0800 44 26 10</div>
  </div>
</header>

<nav class="abs nav">
  <ul>
    <li>Home</li><li>About Us</li><li>Services</li><li>Lawn Care</li><li>Seasonal Care</li><li>Hydroseeding</li><li>FAQs</li><li>Gallery</li><li>Quote / Contact</li>
  </ul>
</nav>

<section class="abs hero">
  <div class="abs hero-lawn" role="img" aria-label="Finished green lawn beside paved paths"></div>
  <div class="abs hero-soil" role="img" aria-label="Prepared bare soil before seeding"></div>
  <div class="abs hero-ring"></div>
  <div class="abs hero-badge">Turf<br>Haven</div>
</section>

<section class="abs intro">
  <h1>YOU CAN ALWAYS SPOT AN TURF HAVEN LAWN</h1>
  <p class="sub">It's the one that turns your neighbours green with envy.</p>
  <p class="body">If you want a lawn or playing field that looks good throughout the year, talk to us. Turf Haven are New Zealand's experts in high quality grass seeding and lawn maintenance, creating the lushest lawns you'll ever see. With high-tech equipment, years of experience and expert aftercare, nobody knows grass like Turf Haven<br>There are many factors that influence the quality of a lawn, including seasonality, growing conditions, shade, seed types, and time. A one-size-fits-all solution couldn't possibly guarantee a great lawn, so we provide personalised advice, a full range of seeding techniques</p>
  <div class="btn">Read more <svg viewBox="0 0 10 10"><circle cx="5" cy="5" r="5" fill="#fff"/><path d="M4 2.8 6.3 5 4 7.2" stroke="#0f6e12" stroke-width="1.4" fill="none"/></svg></div>
</section>

<section class="abs services">
  <article class="card" style="left:103px">
    <div class="pic" role="img" aria-label="Freshly hydroseeded garden bed" style="background:linear-gradient(#4a6a4a,#3d8fa0 60%,#2f6f80)"></div>
    <h3>Grass Seeding Services</h3>
    <p style="top:111px">With a wide range of grass seed applications to choose from, including hydroseeding and instant lawn, there is an option to suit your property and your requirements.</p>
  </article>
  <article class="card" style="left:238px">
    <div class="pic" role="img" aria-label="Sprinkler watering a lawn" style="background:radial-gradient(circle at 50% 60%,#9a6a5a,#5c9a36 40%,#2f6e1c)"></div>
    <h3>Lawn Care Maintenance</h3>
    <p style="top:111px">As well as lawn care services, the team at Turf Haven provides helpful information for regular upkeep of your residential or commercial lawn.</p>
  </article>
  <article class="card" style="left:375px">
    <div class="pic" role="img" aria-label="Lawn around a tree trunk" style="background:linear-gradient(#6a8a5a,#4a8a2e 50%,#3a7a22)"></div>
    <h3>FAQs About Grass<br>Seeding &amp; lawn Care</h3>
    <p style="top:119px">For more information, read our frequently asked questions regarding grass seeding and lawn care.</p>
  </article>
  <article class="card" style="left:514px">
    <div class="pic" role="img" aria-label="Lawn before and after seeding" style="background:linear-gradient(90deg,#3e8a2a 50%,#9a9a8a 50%)"></div>
    <h3>Before and after lawn<br>photos</h3>
    <p style="top:119px">See what you potential new lawn could look like by viewing a range of before and after lawn seeding photos.</p>
  </article>
</section>

<section class="abs welcome">
  <div class="abs video" style="top:705px;top:26px" role="img" aria-label="Video of a lush garden lawn"></div>
  <div class="abs video-play"><svg viewBox="0 0 26 17" width="26" height="17"><path d="M11 5l5 3.5-5 3.5z" fill="#fff"/></svg></div>
  <div class="abs video-bar"></div>
  <div class="abs video-progress"><span></span></div>
  <div class="abs divider-v"></div>
  <h2><em>Welcome To</em> Turf Haven</h2>
  <div class="abs rule"><span></span></div>
  <p class="body">For all things grass, you need the best! Turf Haven are skilled specialists when it comes to creating the perfect lawn for your property.<br>From pre-seeding preparation to a full range of grass seeding services and lawn after care options, you'll enjoy a healthy green lawn for many years.<br>Selling your property? Turf Haven will add the wow factor to the outdoor areas of your home with a lush green lawn.</p>
  <div class="btn">Read more <svg viewBox="0 0 10 10"><circle cx="5" cy="5" r="5" fill="#fff"/><path d="M4 2.8 6.3 5 4 7.2" stroke="#0f6e12" stroke-width="1.4" fill="none"/></svg></div>
</section>

<section class="abs reviews" role="img" aria-label="Lawn mowers on a garden lawn at dusk"></section>
<section class="abs" style="left:0;top:838px;width:739px;height:160px">
  <blockquote style="position:absolute;left:0;width:739px;top:22px;text-align:center;font-family:'Raleway',sans-serif;font-size:11px;color:#fff;line-height:1.3">"I WOULD RECOMMEND TURF HAVEN TO ANYONE WHO<br>WANTS AN AMAZING LAWN"</blockquote>
  <div class="review" style="left:114px"><div class="avatar" role="img" aria-label="Customer portrait"></div><div class="name">LOREM IPSUM DOLOR</div><div class="box">Testimonial here about how great Turf Haven were to deal with and how they are so happy with the lawn and the after care services etc etc."</div></div>
  <div class="review" style="left:300px"><div class="avatar" role="img" aria-label="Customer portrait"></div><div class="name">LOREM IPSUM DOLOR</div><div class="box">Testimonial here about how great Turf Haven were to deal with and how they are so happy with the lawn and the after care services etc etc."</div></div>
  <div class="review" style="left:482px"><div class="avatar" role="img" aria-label="Customer portrait"></div><div class="name">LOREM IPSUM DOLOR</div><div class="box">Testimonial here about how great Turf Haven were to deal with and how they are so happy with the lawn and the after care services etc etc."</div></div>
</section>

<footer class="abs footer">
  <h4>Quick Links</h4>
  <ul class="links">
    <li>Home</li><li>About us</li><li>Services</li><li>Lawn care</li><li>Seasonal care</li><li>Hydroseeding</li><li>FAQs</li><li>Before &amp; After Gallery</li><li>Quote / Contact</li>
  </ul>
  <div class="sep" style="left:201px"></div>
  <div class="abs tree" role="img" aria-label="Illustrated green tree"></div>
  <p class="diploma">Diploma in horticulture</p>
  <div class="sep" style="left:371px"></div>
  <p class="quote">Get a quote for your new lawn!<br>Fill in the form or phone us on 0800 44 26 10.</p>
  <div class="field" style="left:424px;top:56px;width:105px">First name</div>
  <div class="field" style="left:544px;top:56px;width:106px">Last name</div>
  <div class="field" style="left:424px;top:85px;width:105px">Email address</div>
  <div class="field" style="left:544px;top:85px;width:106px">Contact phone</div>
  <div class="field" style="left:424px;top:113px;width:226px;height:43px">Details</div>
</footer>
<div class="abs submit">Submit</div>
<div class="abs copyright">© Copyright 2015. All Rights Reserved</div>

</body>
</html>
```